Bold, Modern, Clean "Quarvenstretch.com" website

Why we stand out?
We are a male and female mobile massage team. Our names are Todd and Lise. 
Quarven Tide is a Seattle based mobile massage service. Our massage is offered to the community with a goal of facilitating balance within each individual. We specialize in integrated Pain management, and sports/medical massage therapy. Every client's first assessment is attended by our male and female massage therapist team. Depending on the goals identified for an individual determines which therapist will be assigned to provide treatment, if not both.

Our passion...
Here at Quarven Tide, we have a great passion for Postural Resoration and how it is integrated into an individual's Massage treatment. We pride ourselves in being natural facilitators of healing, which takes the ego of the therapist out of the client's healing process. We strive to deliver the best massage possible by including modalities such as Neuromuscular, Myofascial release, spontaneous muscle release, postural restoration, orthopedic, and medical massage.

Our education...

We are both Graduates of Halvenor, school of massage therapy. We have continuing education in medical massage, myofacial release, trigger point therapy, postural restoration, anatomy, and spontaneous muscle release. Lise is also a Certified Yoga Instructor, which amplifies her experience with flexibility and strength as it pertains to each individual. Todd's passion is Massage, stretching, and strength training to encourage postural restoration and realignment.

Our rates-

Our rates are $75/ 60 minutes, $95/ 90 minutes, and $120/ 120 minutes.

Education-
Both Lise and I worked as behavioral health professionals that specialized in life skills mentoring for youth who had experienced different types of trauma. This led us both to want to help others in a different environment, where individuals can be empowered to take responsibility over their own healing. To us, massage is a type of manipulation physical therapy, that encourages healing on many levels.

Advice to any massage client-
The most important thing to 'us', as Licenced providers is to get you on to our table to show you our skills. But a good therapist never forgets that it's not about what we do for you, but what we can facilitate for you. Your health and healing has nothing to do with us. It is yours, not ours. Identify what your goals are with any Therapist, and know what the end looks like. Progress should be tangible, such as range of motion, and decreased pain.

5/5 stars Massage Therapy
Verified Review

Lise and Todd at Quarven Tide are awesome! I recently had open heart surgery, and Lise worked on me to increase my range of motion while helping with the pinched nerve from my arm being in the same position for so long during my surgery. My wife drives a lot for work, and Todd has helped decrease her neck and lower back pain immensely. They are seriously the best therapists I have ever worked with. I would recommend them to anyone who needs anything from stress relief to a medical massage treatment. They are professional, up beat, easy going, and always on time. And, I love that they meet us where ever we like! We did a staycation recently, where they came to our hotel to give us relaxation massages. Although usually they come to our home, where we focus on pain related issues. We will continue to work with them for a long, long time.

Bressa K. on December 17, 2015

Target Market(s)

Mobile massage therapy clients

Industry/Entity Type

Massage Therapy

Font styles to use
Serif
Sans Serif

Requirements
Must have
• Please add or remove any information that would help the presentation of our website. Our logo is posted below, please include into the website.
• Please include a contact field that includes, quarvenstretch@mailbrook.net,
• (206) 555-0194
• We have also included our own stock photos, as well as a photo of Todd and Lise. Please include a cropped photo of both massage therapists.

```html
<!DOCTYPE html>
<html lang="en">
<head>
<meta charset="utf-8">
<title>Quarven Tide – Mobile Massage</title>
<link rel="stylesheet" href="https://fonts.googleapis.com/css2?family=Arimo:wght@400;700&family=Dancing+Script:wght@700&family=Josefin+Sans:wght@300;400&display=swap">
<style>
:root{
  --blue:#2f8fc4;
  --blue-deep:#1b6fa3;
  --navy:#1f2a6b;
  --navy-band:#243383;
  --cyan:#27a9d6;
  --ink:#333;
  --muted:#777;
  --grey-bg:#f2f2f2;
  --dark:#1d1d1d;
  --white:#fff;
}
*{box-sizing:border-box;margin:0;padding:0}
html,body{width:1200px;height:2655px;overflow:hidden}
body{position:relative;font-family:"Arimo",Arial,sans-serif;color:var(--ink);background:var(--white)}
.abs{position:absolute}
.script{font-family:"Dancing Script",cursive;font-weight:700}

/* top bar */
.topbar{left:0;top:0;width:1200px;height:39px;background:linear-gradient(#4a4a4a,#2a2a2a);color:#eee;font-size:12px}
.topbar .item{top:12px;display:flex;align-items:center;gap:6px}

/* header */
.header{left:0;top:39px;width:1200px;height:117px;background:var(--white)}
.brand{left:134px;top:45px;width:150px;height:150px;border-radius:50%;background:#1f4fa8;border:7px solid var(--white);box-shadow:0 2px 6px rgba(0,0,0,.2);display:flex;align-items:center;justify-content:center;z-index:3}
.brand span{color:var(--white);font-weight:700;font-size:22px;text-align:center;line-height:1.1}
.nav{top:117px;font-size:11.5px;color:#333;letter-spacing:.2px}
.nav.active{border:2px solid var(--blue);border-radius:16px;padding:5px 14px;top:110px;color:var(--blue-deep);font-weight:700}
.social-dot{width:26px;height:26px;border-radius:50%;background:var(--blue-deep)}

/* hero */
.hero{left:0;top:156px;width:1200px;height:513px;background:linear-gradient(100deg,#8a8c86 0%,#b9bcb5 25%,#6f8f7a 38%,#3fb5cf 55%,#6ccfe0 75%,#9bdde8 100%)}
.caption{left:76px;top:450px;width:434px;height:210px;background:rgba(20,20,20,.72);border:2px solid rgba(255,255,255,.6);outline:6px solid rgba(0,0,0,.35);color:#ddd;text-align:center;font-family:"Josefin Sans",sans-serif}
.caption h1{font-weight:300;font-size:40px;letter-spacing:2px;margin-top:36px}
.caption p{font-size:18px;letter-spacing:1px;line-height:1.6;margin-top:14px;font-weight:300}
.dots{position:absolute;left:50%;bottom:18px;transform:translateX(-50%);display:flex;gap:6px}
.dots i{width:9px;height:9px;border-radius:50%;background:var(--cyan)}
.dots i.on{background:var(--white)}
.consult{left:715px;top:195px;width:372px;height:421px;background:rgba(30,40,45,.82);border:2px solid rgba(255,255,255,.8);outline:5px solid rgba(0,0,0,.3);padding:0 18px}
.consult h2{font-family:"Josefin Sans",serif;font-weight:400;color:var(--white);font-size:22px;text-align:center;margin-top:22px;letter-spacing:1px}
.consult .rule{display:flex;align-items:center;gap:10px;margin:10px 0 14px}
.consult .rule b{flex:1;height:1px;background:var(--cyan)}
.field{background:var(--white);height:40px;margin-bottom:9px;font-size:11px;color:#999;padding:12px 14px}
.field.msg{height:88px}
.submit{background:linear-gradient(#33b6e0,#1996c4);color:var(--white);font-family:"Josefin Sans",sans-serif;font-size:17px;text-align:center;height:52px;line-height:54px;letter-spacing:1px;margin-top:4px}

/* section titles */
.title{left:0;width:1200px;text-align:center;font-size:26px;color:#222}
.lead{left:186px;top:739px;width:832px;font-size:11px;line-height:21.5px;color:var(--muted);text-align:center}

/* passion */
.card{width:301px}
.card .photo{height:177px}
.card .bar{height:9px;background:var(--blue-deep)}
.card h3{text-align:center;color:var(--blue-deep);font-size:18px;margin-top:18px}
.card p{text-align:center;font-size:11px;line-height:17px;color:var(--muted);margin-top:6px}
.arrow{width:20px;height:20px}

/* rates */
.rates{left:0;top:1218px;width:1200px;height:416px;background:var(--grey-bg)}
.rate{width:258px;height:298px;background:var(--white);top:1306px}
.rate .band{height:64px;background:var(--blue)}
.rate .badge{position:absolute;left:85px;top:9px;width:88px;height:88px;border-radius:50%;background:var(--navy);color:var(--white);text-align:center;border:3px solid var(--white)}
.rate .badge b{display:block;font-size:20px;font-weight:400;margin-top:18px}
.rate .badge small{font-size:11px}
.rate ul{list-style:none;text-align:center;font-size:14px;color:#555;margin-top:58px;line-height:27.5px}
.rate .btn{position:absolute;left:0;top:252px;width:258px;height:46px;border:2px solid var(--blue-deep);color:var(--blue-deep);font-size:13px;text-align:center;line-height:42px;background:var(--white)}
.rate .btn.fill{background:var(--blue);color:var(--white);box-shadow:inset 0 0 0 3px var(--white)}

/* education */
.edu{left:0;top:1634px;width:1200px;height:416px;background:radial-gradient(ellipse at 30% 40%,#7e8c55,#3c4a2a 55%,#20281a)}
.edu-card{left:133px;top:1694px;width:941px;height:297px;background:var(--white)}
.edu-photo{left:142px;top:1703px;width:263px;height:279px;background:linear-gradient(160deg,#c8b59a,#e6d7c0 45%,#8fc3cf)}
.edu-side{left:380px;top:1880px;width:25px;height:102px;background:var(--blue-deep);display:flex;flex-direction:column;align-items:center;justify-content:space-around;padding:6px 0}
.edu-side i{width:9px;height:9px;background:var(--white);border-radius:2px}
.edu-text{left:425px;top:1756px;width:640px;font-size:11px;line-height:20.5px;color:#666}
.readmore{left:427px;top:1862px;width:148px;height:33px;background:var(--blue-deep);border:3px solid #cfe3ef;color:var(--white);font-size:10.5px;font-weight:700;display:flex;align-items:center;justify-content:center;gap:10px}
.follow{left:427px;top:1927px;font-size:11px;color:#555}
.follow-dot{top:1915px;width:36px;height:36px;border-radius:50%}
.pager{top:1956px;width:24px;height:22px;background:var(--blue-deep)}

/* testimonials */
.avatar{border-radius:50%;border:5px solid var(--blue)}
.avatar::after{content:"";position:absolute;left:50%;bottom:-14px;transform:translateX(-50%);border:8px solid transparent;border-top-color:var(--blue)}
.t-name{left:0;width:1200px;text-align:center;color:var(--navy);font-style:italic;font-weight:700;font-size:13px;top:2268px}
.t-role{left:0;width:1200px;text-align:center;font-size:10px;color:#555;top:2289px}
.stars{left:563px;top:2311px;display:flex;gap:5px}
.t-text{left:190px;top:2351px;width:820px;text-align:center;font-size:11px;line-height:21.5px;color:#666}

/* footer */
.footer{left:0;top:2487px;width:1200px;height:168px;background:var(--dark)}
.signup{left:120px;top:2448px;width:960px;height:104px;background:linear-gradient(90deg,var(--navy-band),#2c3c95 50%,var(--navy-band))}
.signup h2{position:absolute;left:72px;top:32px;color:var(--white);font-size:30px}
.signup .input{position:absolute;left:487px;top:37px;width:296px;height:32px;background:#e8e8ee;font-size:11px;color:#aaa;padding:9px 12px}
.signup .go{position:absolute;left:783px;top:37px;width:106px;height:32px;background:var(--cyan);color:var(--white);font-size:14px;text-align:center;line-height:32px}
.ficon{top:2590px;width:15px;height:15px;background:#e6e6e6;border-radius:3px}
.copy{left:0;width:1200px;top:2623px;text-align:center;color:#ccc;font-size:11px}
.copy a{color:var(--cyan);text-decoration:none}
</style>
</head>
<body>

<!-- top bar -->
<div class="abs topbar">
  <div class="abs item" style="left:790px">
    <svg width="10" height="14" viewBox="0 0 10 14"><rect x="2" y="0" width="6" height="9" rx="3" fill="#ddd"/><path d="M1 7a4 4 0 0 0 8 0M5 11v3" stroke="#ddd" fill="none" stroke-width="1.3"/></svg>
    (206) 555-0194
  </div>
  <div class="abs item" style="left:905px">
    <svg width="13" height="10" viewBox="0 0 13 10"><rect width="13" height="10" rx="1" fill="#ddd"/><path d="M0 1l6.5 5L13 1" stroke="#444" fill="none"/></svg>
    quarvenstretch@mailbrook.net
  </div>
</div>

<!-- header -->
<div class="abs header"></div>
<div class="abs brand"><span>Quarven<br>Tide</span></div>
<div class="abs nav active" style="left:315px">HOME</div>
<div class="abs nav" style="left:405px">ABOUT US</div>
<div class="abs nav" style="left:503px">OUR PASSION</div>
<div class="abs nav" style="left:620px">OUR PRICE</div>
<div class="abs nav" style="left:722px">TESTIMONIALS</div>
<div class="abs nav" style="left:844px">CONTACT US</div>
<div class="abs social-dot" style="left:970px;top:110px"></div>
<div class="abs social-dot" style="left:1004px;top:110px"></div>
<div class="abs social-dot" style="left:1039px;top:110px"></div>

<!-- hero -->
<div class="abs hero" role="img" aria-label="Stone statue beside green leaves and black massage stones on a turquoise wooden surface"></div>
<div class="abs caption">
  <h1>QUARVEN TIDE</h1>
  <p>SPECIALIZES IN SPORTS AND MEDICAL<br>MASSAGE THERAPY.</p>
  <div class="dots"><i></i><i class="on"></i><i></i></div>
</div>
<form class="abs consult">
  <h2>FREE CASE CONSULTATION</h2>
  <div class="rule"><b></b>
    <svg width="18" height="18" viewBox="0 0 18 18" stroke="#fff" stroke-width="1.2"><path d="M9 1v16M1 9h16M3.3 3.3l11.4 11.4M14.7 3.3L3.3 14.7"/></svg>
  <b></b></div>
  <div class="field">Name</div>
  <div class="field">Phone</div>
  <div class="field">Email address</div>
  <div class="field msg">message</div>
  <div class="submit">SUBMIT NOW</div>
</form>

<!-- why we stand out -->
<h2 class="abs title script" style="top:688px">Why we stand out?</h2>
<p class="abs lead">We are a male and female mobile massage team. Our names are Todd and Lise. Quarven Tide is a Seattle based mobile massage service. Our massage is offered to the community with a goal of facilitating balance within each individual. We specialize in integrated Pain management, and sports/medical massage therapy. Every client's first assessment is attended by our male and female massage therapist team. Depending on the goals identified for an individual determines which therapist will be assigned to provide treatment, if not both.</p>

<!-- our passion -->
<h2 class="abs title script" style="top:841px">Our Passion</h2>
<svg class="abs arrow" style="left:70px;top:1020px" viewBox="0 0 20 20"><path d="M18 10H3M9 4l-6 6 6 6" stroke="#111" stroke-width="2.4" fill="none"/></svg>
<svg class="abs arrow" style="left:1106px;top:1020px" viewBox="0 0 20 20"><path d="M2 10h15M11 4l6 6-6 6" stroke="#111" stroke-width="2.4" fill="none"/></svg>
<div class="abs card" style="left:133px;top:892px">
  <div class="photo" role="img" aria-label="Woman relaxing face down during a neuromuscular massage with flowers in the foreground" style="background:linear-gradient(135deg,#e9e2d0,#d9b48f 55%,#f3eee3)"></div>
  <div class="bar"></div>
  <h3 class="script">Neuromuscular</h3>
  <p>Lorem ipsum dolor sit amet, consetetur sadipscing elitr, sed diam nonumy eirmod tempor invidunt ut labore et dolore magna aliquyam erat, sed diam voluptua.</p>
</div>
<div class="abs card" style="left:450px;top:892px">
  <div class="photo" role="img" aria-label="Hot stones placed along a back during a myofascial release treatment" style="background:linear-gradient(135deg,#7a3a1c,#c46a3a 50%,#e4b48a)"></div>
  <div class="bar"></div>
  <h3 class="script">Myofascial release</h3>
  <p>Lorem ipsum dolor sit amet, consetetur sadipscing elitr, sed diam nonumy eirmod tempor invidunt ut labore et dolore magna aliquyam erat, sed diam voluptua.</p>
</div>
<div class="abs card" style="left:766px;top:892px">
  <div class="photo" role="img" aria-label="Woman resting on a spa table with folded towels and candles" style="background:linear-gradient(135deg,#5a4030,#b28a6c 50%,#e8d9c8)"></div>
  <div class="bar"></div>
  <h3 class="script">spontaneous muscle release</h3>
  <p>Lorem ipsum dolor sit amet, consetetur sadipscing elitr, sed diam nonumy eirmod tempor invidunt ut labore et dolore magna aliquyam erat, sed diam voluptua.</p>
</div>

<!-- rates -->
<div class="abs rates"></div>
<h2 class="abs title script" style="top:1246px">Our Rates</h2>
<div class="abs rate" style="left:133px">
  <div class="band"></div>
  <div class="badge"><b>$75</b><small>per 60 min</small></div>
  <ul><li>This is included</li><li>You even get this</li><li>Yes, this too!</li><li>You even get this</li></ul>
  <div class="btn">Request an Appointment</div>
</div>
<div class="abs rate" style="left:471px">
  <div class="band"></div>
  <div class="badge"><b>$95</b><small>per 90 min</small></div>
  <ul><li>This is included</li><li>You even get this</li><li>Yes, this too!</li><li>You even get this</li></ul>
  <div class="btn fill">Request an Appointment</div>
</div>
<div class="abs rate" style="left:809px">
  <div class="band"></div>
  <div class="badge"><b>$120</b><small>per 120 min</small></div>
  <ul><li>This is included</li><li>You even get this</li><li>Yes, this too!</li><li>You even get this</li></ul>
  <div class="btn">Request an Appointment</div>
</div>

<!-- education -->
<div class="abs edu" role="img" aria-label="Soft-focus background of green foliage and spa stones"></div>
<div class="abs edu-card"></div>
<div class="abs edu-photo" role="img" aria-label="Portrait of a massage therapist"></div>
<div class="abs edu-side"><i></i><i></i><i></i></div>
<h2 class="abs script" style="left:425px;top:1704px;font-size:26px;color:#222">Our Education</h2>
<p class="abs edu-text">We are both Graduates of Halvenor, school of massage therapy. We have continuing education in medical massage, myofacial release, trigger point therapy, postural restoration, anatomy, and spontaneous muscle release. Lise is also a Certified Yoga Instructor, which amplifies her experience with flexibility and strength as it pertains to each individual. Todd's passion is Massage, stretching, and strength training to encourage postural restoration and realignment.</p>
<div class="abs readmore">READ MORE
  <svg width="12" height="12" viewBox="0 0 12 12"><circle cx="6" cy="6" r="6" fill="#fff"/><path d="M5 3.5L7.5 6 5 8.5" stroke="#1b6fa3" stroke-width="1.5" fill="none"/></svg>
</div>
<div class="abs follow">Follow with :</div>
<div class="abs follow-dot" style="left:509px;background:#26a5e0"></div>
<div class="abs follow-dot" style="left:551px;background:#3b5591"></div>
<div class="abs follow-dot" style="left:596px;background:#1c74b3"></div>
<div class="abs follow-dot" style="left:640px;background:#36475b"></div>
<div class="abs follow-dot" style="left:683px;background:#df4a37"></div>
<div class="abs follow-dot" style="left:728px;background:#c8202c"></div>
<svg class="abs pager" style="left:996px" viewBox="0 0 24 22"><path d="M14 6l-5 5 5 5" fill="#fff"/></svg>
<svg class="abs pager" style="left:1022px" viewBox="0 0 24 22"><path d="M10 6l5 5-5 5" fill="#fff"/></svg>

<!-- testimonials -->
<h2 class="abs title script" style="top:2085px">Testimonials</h2>
<svg class="abs" style="left:128px;top:2186px" width="14" height="18" viewBox="0 0 14 18"><path d="M10 3L4 9l6 6" stroke="#8aa0b8" stroke-width="2" fill="none"/></svg>
<svg class="abs" style="left:1055px;top:2186px" width="14" height="18" viewBox="0 0 14 18"><path d="M4 3l6 6-6 6" stroke="#8aa0b8" stroke-width="2" fill="none"/></svg>
<div class="abs avatar" role="img" aria-label="Client photo" style="left:265px;top:2156px;width:78px;height:78px;background:linear-gradient(135deg,#8a5a3a,#d2a07a)"></div>
<div class="abs avatar" role="img" aria-label="Client photo" style="left:407px;top:2156px;width:78px;height:78px;background:linear-gradient(135deg,#d8c4b0,#8c6a5a)"></div>
<div class="abs avatar" role="img" aria-label="Featured client photo" style="left:541px;top:2138px;width:114px;height:114px;background:linear-gradient(135deg,#f2e4d6,#d8b89c)"></div>
<div class="abs avatar" role="img" aria-label="Client photo" style="left:713px;top:2156px;width:78px;height:78px;background:linear-gradient(135deg,#b06a4a,#e8c8b0)"></div>
<div class="abs avatar" role="img" aria-label="Client photo" style="left:855px;top:2156px;width:78px;height:78px;background:linear-gradient(135deg,#6a5030,#c0a060)"></div>
<div class="abs t-name">Lorem ipsum dolor.</div>
<div class="abs t-role">Lorem ipsum</div>
<div class="abs stars">
  <svg width="12" height="12" viewBox="0 0 12 12"><path d="M6 0l1.8 4 4.2.4-3.2 2.8 1 4.2L6 9.2 2.2 11.4l1-4.2L0 4.4 4.2 4z" fill="#1f2a6b"/></svg>
  <svg width="12" height="12" viewBox="0 0 12 12"><path d="M6 0l1.8 4 4.2.4-3.2 2.8 1 4.2L6 9.2 2.2 11.4l1-4.2L0 4.4 4.2 4z" fill="#1f2a6b"/></svg>
  <svg width="12" height="12" viewBox="0 0 12 12"><path d="M6 0l1.8 4 4.2.4-3.2 2.8 1 4.2L6 9.2 2.2 11.4l1-4.2L0 4.4 4.2 4z" fill="#1f2a6b"/></svg>
  <svg width="12" height="12" viewBox="0 0 12 12"><path d="M6 0l1.8 4 4.2.4-3.2 2.8 1 4.2L6 9.2 2.2 11.4l1-4.2L0 4.4 4.2 4z" fill="#1f2a6b"/></svg>
  <svg width="12" height="12" viewBox="0 0 12 12"><path d="M6 0l1.8 4 4.2.4-3.2 2.8 1 4.2L6 9.2 2.2 11.4l1-4.2L0 4.4 4.2 4z" fill="#1f2a6b"/></svg>
</div>
<p class="abs t-text">Lorem ipsum dolor sit amet, consectetur adipiscing elit. Mauris maximus consequat felis non iaculis. Nullam finibus, magna vel congue cursus, dui massa aliquet arcu, commodo porta ipsum lorem imperdiet lectus. Curabitur tellus diam, consectetur ut egestas a, mollis ac est. Quisque sed blandit sapien. Donec in pulvinar felis. Fusce sed nisl rhoncus, tempus nulla et, venenatis justo. Aliquam efficitur maximus sagittis. Pellentesque nec feugiat ante.</p>

<!-- footer -->
<div class="abs footer"></div>
<div class="abs signup">
  <h2 class="script">Sign up for News &amp; Notifications</h2>
  <div class="input">Enter your email address</div>
  <div class="go">SUBMIT</div>
</div>
<div class="abs ficon" style="left:551px"></div>
<div class="abs ficon" style="left:578px"></div>
<div class="abs ficon" style="left:605px"></div>
<div class="abs ficon" style="left:633px;border-radius:50%"></div>
<div class="abs copy">© 2015 <a>quarvenstretch massage</a>. All rights reserved.</div>

</body>
</html>
```